Business Card Upgrade

I have designed our business card using our new logo. I think it needs imporovements. We used to have two cards for our business. One card was for our software business, and the other was for our consulting business. We are now in the process of combining our websites, marketing, name, and a new logo.

Our goal is to have a really sharp professional logo. One reason I designed the card the way I did was that our Titles are sometimes long, and by separating the person's name and title, it shows up very well and the title can be adjusted no matter how long it is. Sometimes the title can be 4 or 5 words or more.

We really like our logo on black as it shows up very nice. Our PMS colors are as follows: 368C and 459C.

The Designer that will be working with us will need to deliver the following:

The front and back of the Business Card Design will need to be delivered in a high quality JPEG, and
The front and back of the Business Card Design in Illustrator Format .ai
Any fonts will need to be sent to us if they are not standard and are required to open the Illustrator file correctly.

To help us get a good idea of the card with a title, please use the title: " Director of Software Development "

NOTE: The chosen designer will be selected to design our new letterhead within 2 weeks from the closing of this contest.

To help us make sure the card design works with longer titles, please use the followign job title on the card:  

"Director of Software and Product Development"

 

ALL DESIGNERS:

1. I appreciate the different angles you are showing the cards, but please be sure and always show the direct view, so I can see the layout and what the person I hand the card will see.

2. Please do not use white.  Please use off white as I don't care for white cards and they get dirty easy and do not represent the designs well.

Dear Designers,

Please provide samples straight one as a viewer of the card will see.  Some of the angles that are presented make it impossible to tell how everything fits, and sometimes even makes areas look skewed. So, please provide a straight sample view.

Pinnacle 400 company executives such as Vice Presidents, and Directors

Software

• Professional looking Card.

Our customers are Directors, Vice Presidents, and Presidents of companies as large as Pinnacle 400 companies. The card needs to get attention wile still looking professional.

Delivery of the finished product in Illustrator Format with any fonts needed to edit the text or open the file.

The card will be a heavy stock with a soft touch coating for that silk feel.

```html
<!DOCTYPE html>
<html lang="en">
<head>
<meta charset="utf-8">
<title>Harbor Gate Logistics – Business Card</title>
<link rel="stylesheet" href="https://fonts.googleapis.com/css2?family=Montserrat:wght@400;600;700&family=Open+Sans:wght@400;600&display=swap">
<style>
  :root {
    --stage: #e8e5df;
    --card: #444444;
    --card-shade: #555555;
    --chevron: #5e5e5e;
    --green: #78be20;
    --tan: #d8cb8a;
    --pattern: #4f4f4f;
  }
  * { margin: 0; padding: 0; box-sizing: border-box; }
  html, body {
    width: 1200px; height: 841px; overflow: hidden;
    background: var(--stage);
  }
  .stage { position: relative; width: 1200px; height: 841px; }
  .card {
    position: absolute; top: 266px;
    width: 540px; height: 309px;
    background: var(--card);
    border-radius: 4px;
    box-shadow: 0 6px 18px rgba(0,0,0,.18);
    overflow: hidden;
    font-family: "Open Sans", sans-serif;
  }
  .card--back { left: 40px; }
  .card--front { left: 620px; }

  /* Back: brand side */
  .brand {
    position: absolute; left: 0; right: 0; top: 96px;
    text-align: center;
    font-family: "Montserrat", sans-serif;
    font-weight: 700;
    color: var(--green);
    text-transform: uppercase;
    line-height: 1.05;
  }
  .brand__line1 { display: block; font-size: 50px; letter-spacing: 3px; }
  .brand__line2 { display: block; font-size: 26px; letter-spacing: 9px; margin-top: 4px; }
  .back-web {
    position: absolute; left: 0; right: 0; bottom: 42px;
    text-align: center;
    font-family: "Montserrat", sans-serif;
    font-size: 10px; letter-spacing: 7px;
    color: var(--tan); text-transform: uppercase;
  }

  /* Front: person side */
  .chevrons { position: absolute; left: 0; top: 0; }
  .person { position: absolute; left: 30px; top: 68px; }
  .person__name {
    display: flex; align-items: center; gap: 8px;
    font-family: "Montserrat", sans-serif; font-weight: 600;
    font-size: 20px; letter-spacing: 1px;
    color: var(--green); text-transform: uppercase;
  }
  .person__marker { width: 14px; height: 14px; background: var(--green); }
  .person__title {
    margin: 6px 0 0 22px;
    font-size: 10px; color: var(--tan);
  }
  .divider {
    position: absolute; left: 292px; top: 124px;
    width: 1px; height: 104px; background: var(--green);
  }
  .contact {
    position: absolute; left: 310px; top: 124px;
    list-style: none; font-size: 10.5px; color: var(--tan);
  }
  .contact__item { display: flex; align-items: flex-start; gap: 9px; margin-bottom: 9px; line-height: 1.35; }
  .contact__icon { width: 11px; height: 11px; flex: none; margin-top: 2px; fill: var(--tan); }
  .edge-pattern {
    position: absolute; left: 0; right: 0; bottom: 18px;
    height: 16px; background: var(--pattern);
  }
</style>
</head>
<body>
<main class="stage">

  <section class="card card--back" aria-label="Card back">
    <h1 class="brand">
      <span class="brand__line1">Harbor Gate</span>
      <span class="brand__line2">Logistics</span>
    </h1>
    <p class="back-web">www.harborgate.com</p>
  </section>

  <section class="card card--front" aria-label="Card front">
    <svg class="chevrons" width="540" height="120" viewBox="0 0 540 120" aria-hidden="true">
      <polyline points="170,-4 250,62 400,62 470,-4" fill="none" stroke="var(--chevron)" stroke-width="9" stroke-linejoin="round"/>
      <polyline points="-4,96 30,118" fill="none" stroke="var(--chevron)" stroke-width="9"/>
    </svg>

    <div class="person">
      <h2 class="person__name"><span class="person__marker"></span>Dana Whitfield</h2>
      <p class="person__title">Director of Software and Product Development</p>
    </div>

    <span class="divider"></span>

    <ul class="contact">
      <li class="contact__item">
        <svg class="contact__icon" viewBox="0 0 12 12"><path d="M6 0a4 4 0 0 0-4 4c0 3 4 8 4 8s4-5 4-8a4 4 0 0 0-4-4zm0 5.6A1.6 1.6 0 1 1 6 2.4a1.6 1.6 0 0 1 0 3.2z"/></svg>
        <span>1480 Cedar Mill Road,<br>AL 36500</span>
      </li>
      <li class="contact__item">
        <svg class="contact__icon" viewBox="0 0 12 12"><path d="M2.4 0 4.5 2.6 3.4 4.2c.8 1.8 2.2 3.2 4.4 4.4l1.6-1.1L12 9.6 10.6 12C5 11.6.4 7 0 1.4z"/></svg>
        <span>555-014-2278</span>
      </li>
      <li class="contact__item">
        <svg class="contact__icon" viewBox="0 0 12 12"><path d="M0 2h12v8H0zM1 3l5 3.6L11 3v-.2H1z"/></svg>
        <span>dana@harborgate.com</span>
      </li>
      <li class="contact__item">
        <svg class="contact__icon" viewBox="0 0 12 12"><circle cx="6" cy="6" r="5.2" fill="none" stroke="var(--tan)" stroke-width="1.2"/><path d="M1 6h10M6 1c-2.4 2.8-2.4 7.2 0 10M6 1c2.4 2.8 2.4 7.2 0 10" fill="none" stroke="var(--tan)" stroke-width="1"/></svg>
        <span>www.harborgate.com</span>
      </li>
    </ul>

    <div class="edge-pattern" role="img" aria-label="Row of small outlined diamond shapes along the lower edge"></div>
  </section>

</main>
</body>
</html>
```